Corvane Web Site - Creating an Award-Winning Website

We need a simple but upscale web site designed in word press.
A new breed boutique Investment Bank. Specializing in select cutting-edge emerging growth company financings with a focus on impact investing.
This is a customer facing site that must instill confidence,be clean, streamline and easy to navigate.

Target Market(s)

Entrepreneurs, Finance professionals, Investors

Industry/Entity Type

Bank

Number of Pages Required

5+ page

Other font styles liked:
• see attached

Requirements
Must have
• Landing page
• About us
• Investors
• Entrepreneurs
• CrowdFunding
• Contact
Nice to have
• Sign up
• Similar look and feel to this site - https://pellandrow.com

```html
<!DOCTYPE html>
<html lang="en">
<head>
<meta charset="utf-8">
<title>Corvane Capital</title>
<link rel="stylesheet" href="https://fonts.googleapis.com/css2?family=Mulish:wght@300;400;600&display=swap">
<style>
:root{
  --blue:#1f75c4;
  --ink:#2b2b2b;
  --muted:#6f6f6f;
  --line:#d9d9d9;
  --soft:#f5f5f5;
  --footer:#555657;
  --footer-text:#e6e6e6;
  --white:#ffffff;
}
*{box-sizing:border-box;margin:0;padding:0}
html,body{width:1200px;height:3475px;overflow:hidden}
body{font-family:"Mulish",sans-serif;color:var(--ink);background:var(--white);position:relative;font-weight:300}
.abs{position:absolute}
.center{text-align:center;left:0;width:1200px}
a{color:inherit;text-decoration:none}

/* header */
.site-header{position:absolute;top:0;left:0;width:1200px;height:116px;background:var(--white)}
.brand{position:absolute;left:96px;top:30px;display:flex;align-items:center;gap:12px}
.brand-dot{width:44px;height:44px;border-radius:50%;border:2px solid var(--blue)}
.brand-name{color:var(--blue);font-size:19px;font-weight:600;letter-spacing:1px}
.main-nav{position:absolute;right:96px;top:50px;display:flex;gap:46px;font-size:14px;font-weight:400}
.main-nav a{padding-bottom:14px}
.main-nav a.active{border-bottom:2px solid var(--blue)}

/* hero */
.hero{position:absolute;top:116px;left:0;width:1200px;height:614px;overflow:hidden}
.hero-photo{position:absolute;inset:0;background:linear-gradient(135deg,#3b3f46 0%,#8b8f93 35%,#d8d6d2 55%,#6b6f74 80%,#2d3036 100%)}
.hero-curve{position:absolute;left:0;bottom:0;width:1200px;height:80px}
.hero-title{top:150px;font-size:76px;color:var(--white);font-weight:300;letter-spacing:1px}
.hero-sub{top:238px;font-size:28px;color:var(--white)}
.hero-btn{position:absolute;top:296px;left:489px;width:220px;height:51px;background:var(--blue);color:var(--white);font-size:19px;font-weight:400;display:flex;align-items:center;justify-content:center}
.hero-arrow{position:absolute;top:210px;width:20px;height:40px}

/* welcome */
.section-title{font-size:41px;font-weight:300;letter-spacing:1px}
.section-title .accent{color:var(--blue)}
.welcome-title{top:722px}
.welcome-text{position:absolute;left:140px;width:920px;font-size:14.5px;line-height:23px;color:var(--muted);text-align:center}

/* services */
.services{position:absolute;top:1012px;left:0;width:1200px;height:638px;background:var(--soft)}
.service-card{position:absolute;top:128px;width:234px;height:347px;background:var(--white)}
.service-photo{height:181px}
.service-card h3{font-size:18px;font-weight:400;margin:17px 18px 10px}
.service-card p{font-size:12.5px;line-height:18px;color:var(--muted);margin:0 18px}
.outline-btn{position:absolute;border:1.5px solid var(--blue);color:var(--blue);font-size:18px;font-weight:400;display:flex;align-items:center;justify-content:center;background:transparent}

/* about */
.about{position:absolute;top:1650px;left:0;width:1200px;height:449px;background:linear-gradient(180deg,#8e969d 0%,#b7bbbf 45%,#9aa0a5 70%,#6c7177 100%)}
.about-title{top:78px;font-size:76px;color:var(--white);font-weight:300}
.about-text{top:178px;font-size:22px;line-height:32px;color:var(--white)}
.light-btn{border-color:var(--white);color:var(--white);font-size:24px}

/* blog */
.blog-card{position:absolute;top:2236px;width:312px}
.blog-photo{height:185px}
.blog-card h3{font-size:19px;font-weight:400;line-height:26px;margin-top:18px}
.blog-card p{font-size:13.5px;line-height:18px;color:var(--muted);margin-top:8px}
.small-btn{position:relative;margin-top:18px;width:125px;height:40px;font-size:16px;gap:10px}

/* contact */
.contact{position:absolute;top:2688px;left:0;width:1200px;height:458px;background:var(--soft)}
.contact-sub{top:118px;font-size:16px;color:var(--muted)}
.field{position:absolute;height:44px;background:var(--white);border:1px solid var(--line);font-size:12px;color:#9a9a9a;padding:14px 16px}

/* footer */
.site-footer{position:absolute;top:3146px;left:0;width:1200px;height:329px;background:var(--footer);color:var(--footer-text)}
.foot-col{position:absolute;top:48px}
.foot-col h4{font-size:17px;font-weight:400;margin-bottom:16px;letter-spacing:.5px}
.foot-col li{list-style:none;font-size:13px;height:30px}
.foot-sep{position:absolute;top:50px;width:1px;height:195px;background:#6e6f70}
.foot-icon{display:inline-block;width:13px;height:13px;vertical-align:-2px;margin-right:12px}
.social{display:flex;gap:8px;margin-top:4px}
.social span{width:36px;height:36px;border-radius:50%;background:var(--blue);border:2px solid var(--white)}
.foot-rule{position:absolute;top:260px;left:100px;width:1000px;height:1px;background:#7a7b7c}
.copyright{position:absolute;top:283px;left:100px;font-size:13px}
</style>
</head>
<body>

<header class="site-header">
  <a class="brand" href="#"><span class="brand-dot"></span><span class="brand-name">CORVANE CAPITAL</span></a>
  <nav class="main-nav">
    <a class="active" href="#">HOME</a>
    <a href="#">ABOUT US</a>
    <a href="#">INVESTORS</a>
    <a href="#">ENTREPRENEURS</a>
    <a href="#">CROWDFUNDING</a>
    <a href="#">CONTACT US</a>
  </nav>
</header>

<section class="hero">
  <div class="hero-photo" role="img" aria-label="Business people reviewing financial documents at a meeting table"></div>
  <svg class="hero-arrow" style="left:30px" viewBox="0 0 20 40"><path d="M15 5 L5 20 L15 35" fill="none" stroke="#fff" stroke-width="2"/></svg>
  <svg class="hero-arrow" style="right:30px" viewBox="0 0 20 40"><path d="M5 5 L15 20 L5 35" fill="none" stroke="#fff" stroke-width="2"/></svg>
  <h1 class="abs center hero-title">CORVANE CAPITAL</h1>
  <p class="abs center hero-sub">We are a Investment company</p>
  <a class="hero-btn" href="#">GET STARTED</a>
  <svg class="hero-curve" viewBox="0 0 1200 80" preserveAspectRatio="none"><path d="M0 80 L0 40 Q700 -30 1200 30 L1200 80 Z" fill="#fff"/></svg>
</section>

<h2 class="abs center section-title welcome-title">WELCOME TO <span class="accent">CORVANE CAPITAL</span></h2>
<p class="welcome-text" style="top:795px">Lorem ipsum dolor sit amet, consectetur adipiscing elit, sed do eiusmod tempor incididunt ut labore et dolore magna aliqua. Ut enim ad minim veniam, quis nostrud exercitation ullamco laboris nisi ut aliquip ex ea commodo consequat.</p>
<p class="welcome-text" style="top:867px">Sed ut perspiciatis unde omnis iste natus error sit voluptatem accusantium doloremque laudantium, totam rem aperiam, eaque ipsa quae ab illo inventore veritatis et quasi architecto beatae vitae dicta sunt explicabo. Nemo enim ipsam voluptatem quia voluptas sit aspernatur aut odit aut fugit, sed quia consequuntur magni dolores eos qui ratione voluptatem sequi nesciunt.</p>

<section class="services">
  <h2 class="abs center section-title" style="top:44px">OUR SERVICES</h2>
  <article class="service-card" style="left:100px">
    <div class="service-photo" role="img" aria-label="Hands working on a laptop beside sketches" style="background:linear-gradient(135deg,#d9dcdf,#8d9298)"></div>
    <h3>EXERCITATION ULLAM</h3>
    <p>Sed do eiusmod tempor incididunt ut labore et dolore magna aliqua quis nostrud exercitation ullamco laboris nisi ut aliquip.</p>
  </article>
  <article class="service-card" style="left:356px">
    <div class="service-photo" role="img" aria-label="Person using a tablet showing charts" style="background:linear-gradient(135deg,#e6e8ea,#a7b3bd)"></div>
    <h3>OCCAECAT CUPIDAT</h3>
    <p>Ut enim ad minima veniam, quis nostrum exercitationem ullam corporis suscipit laboriosam, nisi ut aliquid ex ea commodi.</p>
  </article>
  <article class="service-card" style="left:611px">
    <div class="service-photo" role="img" aria-label="Hand stacking coins" style="background:linear-gradient(180deg,#ece9e6,#b08a5c)"></div>
    <h3>VOLUPTATEM QUIA</h3>
    <p>But I must explain to you how all this mistaken idea of denouncing pleasure and praising pain was born and I will give you.</p>
  </article>
  <article class="service-card" style="left:866px">
    <div class="service-photo" role="img" aria-label="Hand pointing at charts on a monitor" style="background:linear-gradient(135deg,#c9d6e4,#6f8fb4)"></div>
    <h3>NUMQUAM EIUS MODI</h3>
    <p>At vero eos et accusamus et iusto odio dignissimos ducimus qui blanditiis praesentium voluptatum deleniti atque.</p>
  </article>
  <a class="outline-btn" href="#" style="top:533px;left:519px;width:160px;height:38px">VIEW MORE</a>
</section>

<section class="about" role="img" aria-label="Blurred modern office interior with people walking">
  <h2 class="abs center about-title">ABOUT US</h2>
  <p class="abs center about-text">We are a new breed boutique Investment Bank. Specialising in select cutting-edge<br>emerging growth company financings with a focus on impact investing.</p>
  <a class="outline-btn light-btn" href="#" style="top:310px;left:494px;width:210px;height:47px">READ MORE</a>
</section>

<h2 class="abs center section-title" style="top:2148px">OUR BLOG</h2>
<article class="blog-card" style="left:104px">
  <div class="blog-photo" role="img" aria-label="Advisor meeting with a client at a desk" style="background:linear-gradient(135deg,#eef0f2,#a9b9c8)"></div>
  <h3>EIUSMOD TEMPOR INCIDIDUNT LABORE MAGNA</h3>
  <p>Quis autem vel eum iure reprehenderit qui in ea voluptate velit esse quam nihil dolorem eum quo voluptas..</p>
  <a class="outline-btn small-btn" href="#">View More <svg width="8" height="12" viewBox="0 0 8 12"><path d="M1 1 L6 6 L1 11" fill="none" stroke="currentColor" stroke-width="1.6"/></svg></a>
</article>
<article class="blog-card" style="left:445px">
  <div class="blog-photo" role="img" aria-label="Team working with laptops around a table, seen from above" style="background:linear-gradient(135deg,#8fc9c4,#d9b98a)"></div>
  <h3>EIUSMOD TEMPOR INCIDIDUNT LABORE MAGNA</h3>
  <p>Quis autem vel eum iure reprehenderit qui in ea voluptate velit esse quam nihil dolorem eum quo voluptas..</p>
  <a class="outline-btn small-btn" href="#">View More <svg width="8" height="12" viewBox="0 0 8 12"><path d="M1 1 L6 6 L1 11" fill="none" stroke="currentColor" stroke-width="1.6"/></svg></a>
</article>
<article class="blog-card" style="left:785px">
  <div class="blog-photo" role="img" aria-label="Business handshake over a desk" style="background:linear-gradient(135deg,#3a3a3c,#c9a77d)"></div>
  <h3>EIUSMOD TEMPOR INCIDIDUNT LABORE MAGNA</h3>
  <p>Quis autem vel eum iure reprehenderit qui in ea voluptate velit esse quam nihil dolorem eum quo voluptas..</p>
  <a class="outline-btn small-btn" href="#">View More <svg width="8" height="12" viewBox="0 0 8 12"><path d="M1 1 L6 6 L1 11" fill="none" stroke="currentColor" stroke-width="1.6"/></svg></a>
</article>

<section class="contact">
  <h2 class="abs center section-title" style="top:44px">GET IN TOUCH</h2>
  <p class="abs center contact-sub">If your have a any quries and any information contact us today!</p>
  <div class="field" style="top:162px;left:100px;width:238px">First name</div>
  <div class="field" style="top:162px;left:354px;width:239px">Last name</div>
  <div class="field" style="top:162px;left:609px;width:239px">Email address</div>
  <div class="field" style="top:162px;left:864px;width:236px">Phone number</div>
  <div class="field" style="top:224px;left:100px;width:1000px;height:77px">Message</div>
  <a class="outline-btn" href="#" style="top:345px;left:496px;width:208px;height:53px;font-size:20px">SUBMIT NOW !</a>
</section>

<footer class="site-footer">
  <div class="foot-col" style="left:100px"><h4>COMPANY</h4><ul><li>Home</li><li>About us</li><li>Investors</li><li>Entrepreneurs</li><li>Crowdfunding</li></ul></div>
  <div class="foot-sep" style="left:248px"></div>
  <div class="foot-col" style="left:301px"><h4>SERVICES</h4><ul><li>Planning</li><li>Investment</li><li>Management</li><li>Support</li><li>Others</li></ul></div>
  <div class="foot-sep" style="left:448px"></div>
  <div class="foot-col" style="left:498px"><h4>GET IN TOUCH</h4><ul>
    <li><svg class="foot-icon" viewBox="0 0 16 16"><path d="M3 1 L6 1 L7 5 L5 6.5 Q6.5 9.5 9.5 11 L11 9 L15 10 L15 13 Q15 15 13 15 Q1 14 1 3 Q1 1 3 1Z" fill="currentColor"/></svg>Call us on (01) 55501234</li>
    <li><svg class="foot-icon" viewBox="0 0 16 16"><rect x="1" y="3" width="14" height="10" fill="currentColor"/><path d="M1 3 L8 9 L15 3" fill="none" stroke="#555657" stroke-width="1.4"/></svg>hello@corvanemail.com</li>
  </ul></div>
  <div class="foot-sep" style="left:740px"></div>
  <div class="foot-col" style="left:785px"><h4>WHY US</h4><ul><li>Customers</li><li>Team</li><li>FAQ</li><li>Contact</li></ul></div>
  <div class="foot-sep" style="left:900px"></div>
  <div class="foot-col" style="left:941px"><h4>FOLLOW US</h4><ul><li>Please connect with us on</li></ul>
    <div class="social"><span></span><span></span><span></span><span></span></div>
  </div>
  <div class="foot-rule"></div>
  <p class="copyright">© 2016 Corvane Capital. &nbsp;All right reserved. &nbsp;Term of Use</p>
</footer>

</body>
</html>
```